U.S. Popcorn company needs business cards

We are a popcorn company that manufactures popcorn and sells it to grocery stores worldwide. Our theme is "Americana" and our logo is Kettle Mesa Byway which is the most famous highway in the U.S.

We would like the design to be simple and to use both sides. On the back side we would like to see just the logo and website. The front would be normal details

Target Market(s)

Wholesalers, grocers and distributors

Industry/Entity Type

Manufacture

Contact Information for Business Card

Business name: Kettle Mesa Popcorn
Phone: +1 555 014 2286
Email: Dale@kettlemesapopcorn.com
website: www.kettlemesapopcorn.com
Tag Line: "Fresh from the kettle"
Name: Dale Whitcombe
Title: Founder/President

Requirements
Must have
• Either this design should be fun or clean and simple. I will let you show me your thougths.
Nice to have
• Anything that ties in the real Kettle Mesa Byway.
• Colors might need to be red, white and blue incorporated.
Should not have
• Not be too busy.

```html
<!DOCTYPE html>
<html lang="en">
<head>
<meta charset="utf-8">
<title>Kettle Mesa Popcorn — Business Cards</title>
<link href="https://fonts.googleapis.com/css2?family=Roboto:wght@400;500;700&family=Comic+Neue:wght@700&display=swap" rel="stylesheet">
<style>
  :root {
    --red: #e02127;
    --navy: #1f2f6e;
    --white: #ffffff;
    --stage: #d9d9dc;
    --road-light: #f4f4f4;
    --road-mid: #d2d4d6;
  }
  * { box-sizing: border-box; margin: 0; padding: 0; }
  html, body { width: 1200px; height: 900px; overflow: hidden; }
  body {
    background: var(--stage);
    font-family: "Roboto", Arial, sans-serif;
    position: relative;
  }
  .card {
    position: absolute;
    left: 250px;
    width: 700px;
    height: 400px;
    box-shadow: 0 6px 18px rgba(0,0,0,.25);
    overflow: hidden;
  }
  .brand-mark {
    position: absolute;
    display: flex;
    align-items: center;
    gap: 14px;
    font-family: "Roboto", Arial, sans-serif;
    font-weight: 700;
    white-space: nowrap;
  }
  .brand-dot {
    width: 24px; height: 24px; border-radius: 50%;
    background: currentColor;
    flex: none;
  }

  /* Back side */
  .card--back { top: 40px; background: var(--red); }
  .card--back .brand-mark {
    left: 0; right: 0; top: 130px;
    justify-content: center;
    color: var(--white);
    font-size: 44px;
  }
  .tagline {
    position: absolute;
    left: 0; right: 0; top: 250px;
    text-align: center;
    font-family: "Comic Neue", "Comic Sans MS", cursive;
    font-weight: 700;
    font-size: 30px;
    color: var(--white);
  }

  /* Front side */
  .card--front { top: 460px; background: var(--white); }
  .road-photo {
    position: absolute; inset: 0;
    background: linear-gradient(180deg, var(--white) 0%, var(--road-light) 35%, var(--road-mid) 55%, var(--road-light) 100%);
    opacity: .85;
  }
  .holder { position: absolute; left: 50px; top: 45px; }
  .holder__name { font-size: 30px; font-weight: 500; color: var(--navy); line-height: 1.1; }
  .holder__title { font-size: 15px; color: var(--red); margin-top: 4px; }
  .card--front .brand-mark {
    right: 40px; top: 125px;
    color: var(--navy);
    font-size: 32px;
  }
  .contacts {
    position: absolute; left: 50px; top: 225px;
    list-style: none;
    font-size: 18px; color: var(--navy);
  }
  .contacts li { display: flex; align-items: center; gap: 12px; margin-bottom: 8px; }
  .contacts svg { width: 18px; height: 18px; flex: none; }
  .website {
    position: absolute; right: 40px; bottom: 28px;
    font-size: 22px; color: var(--navy);
  }
</style>
</head>
<body>

<section class="card card--back" aria-label="Card back">
  <div class="brand-mark"><span class="brand-dot"></span>Kettle Mesa Popcorn</div>
  <p class="tagline">“Fresh from the kettle”</p>
</section>

<section class="card card--front" aria-label="Card front">
  <div class="road-photo" role="img" aria-label="Faded photograph of an open desert highway stretching to the horizon under a pale sky"></div>

  <div class="holder">
    <h1 class="holder__name">Dale Whitcombe</h1>
    <p class="holder__title">Founder/President</p>
  </div>

  <div class="brand-mark"><span class="brand-dot"></span>Kettle Mesa Popcorn</div>

  <ul class="contacts">
    <li>
      <svg viewBox="0 0 24 24" aria-hidden="true"><path fill="#e02127" d="M6.6 10.8a15 15 0 0 0 6.6 6.6l2.2-2.2a1 1 0 0 1 1-.25 11.4 11.4 0 0 0 3.6.6 1 1 0 0 1 1 1V20a1 1 0 0 1-1 1A17 17 0 0 1 3 4a1 1 0 0 1 1-1h3.5a1 1 0 0 1 1 1c0 1.25.2 2.45.6 3.6a1 1 0 0 1-.25 1z"/></svg>
      +1 555 014 2286
    </li>
    <li>
      <svg viewBox="0 0 24 24" aria-hidden="true"><rect x="2" y="5" width="20" height="14" rx="1.5" fill="none" stroke="#e02127" stroke-width="2"/><path d="M3 6l9 7 9-7" fill="none" stroke="#e02127" stroke-width="2"/></svg>
      Dale@kettlemesapopcorn.com
    </li>
    <li>
      <svg viewBox="0 0 24 24" aria-hidden="true"><circle cx="12" cy="12" r="9" fill="none" stroke="#e02127" stroke-width="2"/><path d="M3 12h18M12 3c3 3 3 15 0 18M12 3c-3 3-3 15 0 18" fill="none" stroke="#e02127" stroke-width="1.6"/></svg>
      www.kettlemesapopcorn.com
    </li>
  </ul>

  <p class="website">www.kettlemesapopcorn.com</p>
</section>

</body>
</html>
```